Thriving Mexican import business needs a new business card

Need a refresher of our current business card. Looking for a lighter background with the logo on one side. We will want this file to be adjustable so we can change names, emails and mobile numbers.
We are open to ideas but maintaining a professional image is critical.
Thankyou,

Target Market(s)

Anyone in food industry

Industry/Entity Type

Wholesale

Contact Information for Business Card

Mark Pendlebury
Director
Condor Provisions & Spirits Pty Ltd
5B Morrow Ct, Kelvinbrook VIC 3127
0421930576 (03) 95128460
mark@condorlatino.example.au
condorlatinoprovisionsandspirits.example.au

Font styles to use
Serif
Other font styles liked:
• NeoGram Heavy

Requirements
Must have
• Professional yet memorable
Condor logo
Nice to have
• Chilli or tequila/mexican food pictures
Should not have
• Dark background

```html
<!DOCTYPE html>
<html lang="en">
<head>
<meta charset="utf-8">
<title>Condor Provisions &amp; Spirits – Business Card</title>
<link rel="stylesheet" href="https://fonts.googleapis.com/css2?family=Barlow+Condensed:wght@400;500;600;700&display=swap">
<style>
  :root {
    --backdrop: #e2e2e2;
    --card: #f4f4f4;
    --flag-green: #106546;
    --flag-red: #c62127;
    --ink: #1d1b1b;
    --ink-soft: #2a2a2a;
    --chilli-red: #d22a1e;
    --chilli-yellow: #f2b21c;
    --chilli-green: #4d8a2a;
  }
  * { margin: 0; padding: 0; box-sizing: border-box; }
  html, body {
    width: 1200px; height: 960px; overflow: hidden;
    background: var(--backdrop);
    font-family: "Barlow Condensed", "Arial Narrow", sans-serif;
    color: var(--ink);
  }
  .card {
    position: absolute; left: 311px; width: 580px; height: 354px;
    background: var(--card); overflow: hidden;
  }
  .card--front { top: 105px; display: flex; }
  .card--back { top: 503px; }

  /* Front */
  .stripe { flex: 1 1 0; height: 100%; }
  .stripe--green { background: var(--flag-green); }
  .stripe--white { background: var(--card); }
  .stripe--red { background: var(--flag-red); }

  .front-brand {
    position: absolute; left: 193px; width: 194px; top: 91px;
    display: flex; flex-direction: column; align-items: center;
  }
  .brand-square { width: 60px; height: 60px; background: var(--ink); }
  .brand-name {
    margin-top: 16px; font-weight: 700; font-size: 64px; line-height: 56px;
    letter-spacing: 0.5px; color: var(--ink); text-transform: uppercase;
  }
  .chilli-image {
    position: absolute; left: 146px; top: 275px; width: 288px; height: 42px;
    border-radius: 21px;
    background: linear-gradient(90deg, var(--chilli-red) 0%, var(--chilli-green) 28%, var(--chilli-yellow) 45%, var(--chilli-red) 62%, var(--chilli-yellow) 78%, var(--chilli-green) 100%);
  }

  /* Back */
  .back-brand {
    position: absolute; left: 115px; top: 98px; width: 148px; height: 62px;
    display: flex; align-items: center; justify-content: flex-end; gap: 10px;
  }
  .back-brand .brand-square { width: 40px; height: 40px; }
  .back-brand .brand-name { margin: 0; font-size: 44px; line-height: 44px; }

  .divider {
    position: absolute; left: 289px; top: 98px; width: 2px; height: 150px;
    background: var(--ink);
  }
  .company-address {
    position: absolute; right: 317px; top: 193px; text-align: right;
    font-size: 15px; line-height: 19px; font-weight: 400;
  }
  .company-address strong { font-weight: 700; }

  .person { position: absolute; left: 317px; top: 104px; }
  .person-name { font-size: 23px; font-weight: 500; line-height: 26px; text-transform: uppercase; }
  .person-role { font-size: 15px; line-height: 18px; text-transform: uppercase; margin-top: 3px; }

  .contact-list { position: absolute; left: 317px; top: 193px; list-style: none; font-size: 15px; line-height: 19px; }
  .contact-list li { display: flex; align-items: center; gap: 4px; }
  .contact-list svg { width: 13px; height: 13px; fill: var(--ink); flex: none; }

  .website {
    position: absolute; left: 0; right: 0; top: 304px; text-align: center;
    font-size: 16px; letter-spacing: 1.6px; font-weight: 400; color: var(--ink-soft);
  }
  .website b { font-weight: 700; color: var(--ink); }
</style>
</head>
<body>

<section class="card card--front" aria-label="Card front">
  <div class="stripe stripe--green"></div>
  <div class="stripe stripe--white"></div>
  <div class="stripe stripe--red"></div>
  <div class="front-brand">
    <div class="brand-square"></div>
    <div class="brand-name">Condor</div>
  </div>
  <div class="chilli-image" role="img" aria-label="Photograph of a row of sliced red, yellow and green chillies"></div>
</section>

<section class="card card--back" aria-label="Card back">
  <div class="back-brand">
    <div class="brand-square"></div>
    <div class="brand-name">Condor</div>
  </div>

  <div class="company-address">
    <strong>Condor Provisions &amp; Spirits Pty Ltd</strong><br>
    5B Morrow Ct,<br>
    Kelvinbrook VIC 3127
  </div>

  <div class="divider"></div>

  <div class="person">
    <div class="person-name">Mark Pendlebury</div>
    <div class="person-role">Director</div>
  </div>

  <ul class="contact-list">
    <li>
      <svg viewBox="0 0 16 16" aria-hidden="true"><path d="M3.6 1 6 3.4 4.7 5.6a9 9 0 0 0 5.7 5.7L12.6 10 15 12.4l-1.6 2.4C7 14.4 1.6 9 1.2 2.6Z"/></svg>
      0421 93 05 76
    </li>
    <li>
      <svg viewBox="0 0 16 16" aria-hidden="true"><path d="M4.5 0h7A1.5 1.5 0 0 1 13 1.5v13a1.5 1.5 0 0 1-1.5 1.5h-7A1.5 1.5 0 0 1 3 14.5v-13A1.5 1.5 0 0 1 4.5 0Zm.5 2v10h6V2Zm3 11a1 1 0 1 0 0 2 1 1 0 0 0 0-2Z"/></svg>
      (03) 9512 8460
    </li>
    <li>
      <svg viewBox="0 0 16 16" aria-hidden="true"><path d="M0 3h16v10H0Zm1.5 1.5v.3L8 9l6.5-4.2v-.3Zm0 2.1v5h13v-5L8 10.8Z"/></svg>
      mark@condorlatino.example.au
    </li>
  </ul>

  <div class="website"><b>condor</b>latino<b>provisions</b>and<b>spirits</b>.example.au</div>
</section>

</body>
</html>
```